**Kestrel Joinery Works Limited**

We need a website for a renovation/remodeling company based in Hamilton, New Zealand. Ideally it will catch clients' attention and be modern and professional looking. I have attached a logo that I have just recently had made (through PixelForge). If the website could reflect this style and colour schemes, that would be awesome. The final design should communicate a trustworthiness and professionalism.

I have attached photos of a website that I really think is great, so if we could have something that follows along those likes,

https://www.dailyquillpost.example/local-news/news/hamilton-builder-named-top-apprentice-in-region/QXPLTZ8VRA3MJ5FDYHUNCESKWB/

I won a competition a few years ago while I was an apprentice, If we could somehow put that in there as one of my achievements to try to bring in some trust that would be awesome. I would like to add a new picture though because my beard in that photo is wild.

Target Market(s)

Families that want live in the homes that i'm working on. not investors. People that are looking for quality not cheapest price.

Industry/Entity Type

Construction, Home renovations, Maintenance, Deck Builds, New Builds, Bathrooms, Kitchens

Coding

Number of Pages Required

5+ page

Font styles to use
Sans Serif

Colors
6B429C
8869AF
B7A5CE
E3DAEB
F3F0F8

Requirements
Must have
• Contact us page, large clear pictures, Colours the work with the purple in my logo. That will be my company colour so I'm thinking black and purple, or what ever compliments purple nicely
Nice to have
• Page for Renovations, Testimonials, Contact us, Home, About us
Should not have
• Plain looking pages, empty white space, I want the text to be beside a nice big picture etc

```html
<!DOCTYPE html>
<html lang="en">
<head>
<meta charset="utf-8">
<title>Kestrel Joinery Works</title>
<link href="https://fonts.googleapis.com/css2?family=Playfair+Display:wght@700;900&family=Poppins:wght@400;500;600&display=swap" rel="stylesheet">
<style>
:root{
  --purple:#6B429C;
  --purple-mid:#8869AF;
  --purple-soft:#B7A5CE;
  --lilac:#E3DAEB;
  --mist:#F3F0F8;
  --ink:#1f1b24;
  --dark:#2d2a30;
  --white:#ffffff;
}
*{margin:0;padding:0;box-sizing:border-box}
html,body{width:1200px;height:4234px;overflow:hidden}
body{position:relative;font-family:'Poppins',sans-serif;color:var(--ink);background:var(--white)}
.abs{position:absolute}
.serif{font-family:'Playfair Display',serif;font-weight:900}
.btn{position:absolute;display:flex;align-items:center;justify-content:center;gap:12px;border-radius:30px;font-size:13px;font-weight:500}
.btn svg{width:24px;height:10px}

/* nav */
.nav{left:0;top:0;width:1200px;height:113px;background:var(--mist)}
.brand{left:160px;top:40px;display:flex;align-items:center;gap:10px;font-size:15px;font-weight:600;color:var(--purple)}
.brand i{width:18px;height:18px;background:var(--purple);display:block}
.nav-home{left:562px;top:20px;width:64px;height:80px;background:var(--lilac);border-radius:32px 32px 0 0}
.nav-link{top:40px;font-size:13px;color:var(--ink)}
.nav-cta{left:893px;top:26px;width:147px;height:46px;background:var(--purple);color:var(--white)}

/* hero */
.hero{left:0;top:113px;width:1200px;height:564px;background:linear-gradient(100deg,#4a4548 0%,#6e6662 40%,#857a70 65%,#3a3537 100%)}
.hero-ring{border-radius:50%;border:2px solid rgba(255,255,255,.9)}
.hero-title{left:0;top:250px;width:1200px;text-align:center;color:var(--white);font-size:40px;line-height:57px}
.hero-title u{text-decoration-thickness:2px;text-underline-offset:6px}
.hero-copy{left:310px;top:364px;width:580px;text-align:center;color:var(--white);font-size:16px;line-height:30px}
.hero-badge{left:582px;top:434px;width:36px;height:36px;border-radius:50%;background:var(--white);border:3px solid #b8d36a}
.hero-cta{left:528px;top:485px;width:144px;height:44px;background:var(--white);color:var(--purple)}
.hero-bar{left:600px;top:677px;width:600px;height:7px;background:var(--purple)}

/* about */
.about{left:0;top:759px;width:1200px;height:607px;background:var(--purple)}
.photo{position:absolute}
.about-photo{left:160px;top:808px;width:434px;height:508px;border:3px solid var(--white);background:linear-gradient(180deg,#e9e6e2 0%,#c9c3bb 55%,#8c6b4c 100%)}
.about-panel{left:594px;top:843px;width:496px;height:392px;background:rgba(80,45,125,.55)}
.eyebrow{font-size:12px;letter-spacing:.2px;color:var(--lilac);text-transform:uppercase;display:flex;align-items:center;gap:22px}
.eyebrow::after{content:"";width:70px;height:1px;background:var(--lilac)}
.about-h{color:var(--white);font-size:30px}
.about-copy{color:var(--white);font-size:13.5px;line-height:22.5px;font-weight:500}
.about-cta{left:632px;top:1196px;width:168px;height:46px;background:var(--white);color:var(--purple)}

/* renovations */
.reno{left:0;top:1441px;width:1200px;height:419px;background:var(--mist)}
.reno-h{left:0;top:1482px;width:1200px;text-align:center;font-size:46px;color:var(--ink)}
.reno-copy{left:250px;top:1556px;width:700px;text-align:center;font-size:13.5px;line-height:22.5px;color:#3a3540}
.cat{top:1680px;width:150px;text-align:center;font-size:13px}
.cat .dot{width:100px;height:100px;border-radius:50%;margin:0 auto 18px;border:3px solid var(--white);box-shadow:0 2px 6px rgba(0,0,0,.15)}
.arrow-circ{width:38px;height:38px;border-radius:50%;border:1.5px solid var(--purple);display:flex;align-items:center;justify-content:center}
.arrow-circ svg{width:14px;height:14px}
.reno-photo{left:0;top:1860px;width:1200px;height:410px;background:linear-gradient(90deg,#7d6d59 0%,#ece2cf 35%,#f4ebdc 55%,#d8c7a8 80%,#8a7a63 100%)}
.reno-bar{left:147px;top:2270px;width:905px;height:12px;background:var(--purple)}
.get-started{left:419px;top:2317px;width:165px;height:44px;background:var(--purple);color:var(--white)}
.learn-more{left:615px;top:2317px;width:166px;height:44px;border:1.5px solid var(--purple);color:var(--purple)}

/* architectural */
.arch{left:0;top:2438px;width:1200px;height:607px;background:linear-gradient(90deg,#6B429C 0%,#7450a3 60%,#6B429C 100%)}
.arch-photo{left:608px;top:2476px;width:435px;height:531px;border:3px solid var(--white);background:linear-gradient(180deg,#e6e2dc 0%,#d9d2c8 50%,#2b2a2c 100%)}
.arch-copy{font-size:13px;line-height:22.5px}
.arch-cta{left:160px;top:2862px;width:168px;height:46px;background:var(--white);color:var(--purple)}

/* testimonials */
.testi-h{left:0;top:3106px;width:1200px;text-align:center;font-size:31px;color:var(--ink)}
.testi-sub{left:0;top:3155px;width:1200px;text-align:center;font-size:13px}
.testi-card{left:158px;top:3230px;width:433px;height:465px;background:var(--lilac)}
.testi-photo{left:624px;top:3230px;width:415px;height:465px;background:linear-gradient(180deg,#f1efeb 0%,#e4e1db 60%,#cfcac3 100%)}
.quote-mark{left:188px;top:3268px;font-size:250px;line-height:220px;height:110px;overflow:hidden;color:var(--purple)}
.stars{left:194px;top:3398px;display:flex;gap:3px}
.stars svg{width:21px;height:21px}
.testi-copy{left:194px;width:375px;font-size:13px;line-height:16.5px;color:#3b3641}
.avatar{left:184px;top:3586px;width:78px;height:78px;border-radius:50%;border:3px solid var(--purple);background:linear-gradient(135deg,#8d7a5a,#c7b894)}
.who{left:272px;top:3608px;font-size:12.5px;font-weight:500}
.who small{display:block;font-size:11px;font-weight:400;margin-top:2px}

/* footer */
.footer{left:0;top:3770px;width:1200px;height:464px;background:var(--dark)}
.foot-brand{left:160px;top:3900px;display:flex;align-items:center;gap:10px;font-size:18px;font-weight:600;color:var(--white)}
.foot-brand i{width:22px;height:22px;background:var(--white);display:block}
.foot-copy{left:160px;top:3972px;width:300px;font-size:13.5px;line-height:22.5px;color:var(--white);font-weight:500}
.foot-h{top:3887px;font-size:25px;font-weight:600;color:var(--white)}
.foot-link{left:558px;font-size:13px;color:var(--white)}
.info{left:776px;display:flex;gap:14px;font-size:13px;line-height:22px;color:var(--white);width:280px}
.info svg{flex:none;width:18px;height:18px;margin-top:2px}
.foot-line{left:0;top:4188px;width:1200px;height:1px;background:rgba(255,255,255,.25)}
.legal{top:4205px;font-size:12.5px;color:var(--white)}
</style>
</head>
<body>

<!-- navigation -->
<header class="abs nav"></header>
<div class="abs brand"><i></i>Kestrel Joinery Works</div>
<div class="abs nav-home"></div>
<span class="abs nav-link" style="left:571px;color:var(--purple)">Home</span>
<span class="abs nav-link" style="left:657px">Renovations</span>
<span class="abs nav-link" style="left:786px">About us</span>
<div class="btn nav-cta">Contact us</div>

<!-- hero -->
<section class="abs hero" role="img" aria-label="Carpenter workshop with a white hard hat and work gloves"></section>
<div class="abs hero-ring" style="left:77px;top:168px;width:46px;height:46px"></div>
<div class="abs hero-ring" style="left:99px;top:380px;width:164px;height:164px;background:rgba(220,215,210,.35)" role="img" aria-label="Close-up of a hard hat fitting"></div>
<div class="abs hero-ring" style="left:967px;top:237px;width:320px;height:320px;background:rgba(60,50,50,.45)" role="img" aria-label="Close-up of a work glove holding tools"></div>
<h1 class="abs hero-title serif"><u>KESTREL JOINERY WORKS RENOVATIONS</u><br>CONSTRUCTION</h1>
<p class="abs hero-copy">Lorem ipsum dolor sit amet, consectetur adipiscing elit, sed do eius-mod tempor incididunt ut labore et dolore lacus vel facilisis.</p>
<div class="abs hero-badge"></div>
<div class="btn hero-cta">Contact Now</div>
<div class="abs hero-bar"></div>

<!-- about -->
<section class="abs about"></section>
<div class="photo about-photo" role="img" aria-label="Carpenter in a hard hat fitting a ceiling light on scaffolding"></div>
<div class="abs about-panel"></div>
<div class="abs eyebrow" style="left:632px;top:878px">Constrution &amp; Real Estate Executive Recruiters</div>
<h2 class="abs about-h serif" style="left:632px;top:910px">About Us</h2>
<p class="abs about-copy" style="left:632px;top:966px;width:415px">Lorem ipsum dolor sit amet, consectetur adipiscing elit, sed do eiusmod tempor incididunt ut labore et dolore magna aliqua. Quis ipsum suspendisse ultrices gravida. Risus commodo viverra maecenas accumsan lacus vel facilisis.</p>
<p class="abs about-copy" style="left:632px;top:1079px;width:415px">Lorem ipsum dolor sit amet, consectetur adipiscing elit, sed do eiusmod tempor incididunt ut labore et dolore magna aliqua. Quis ipsum suspendisse ultrices gravida. Risus commodo viverra maecenas accumsan lacus vel facilisis.</p>
<div class="btn about-cta">Learn More<svg viewBox="0 0 24 10"><path d="M0 5h22M17 1l5 4-5 4" fill="none" stroke="currentColor" stroke-width="1.5"/></svg></div>

<!-- renovations -->
<section class="abs reno"></section>
<h2 class="abs reno-h serif">Renovations</h2>
<p class="abs reno-copy">Lorem ipsum dolor sit amet, consectetur adipiscing elit, sed do eiusmod tempor incididunt ut labore et dolore magna aliqua. Quis ipsum suspendisse ultrices gravida. Risus commodo viverra maecenas ac-cumsan lacus vel facilisis.</p>
<div class="abs arrow-circ" style="left:84px;top:1710px"><svg viewBox="0 0 14 14"><path d="M9 2L4 7l5 5" fill="none" stroke="var(--purple)" stroke-width="1.6"/></svg></div>
<div class="abs arrow-circ" style="left:1076px;top:1710px"><svg viewBox="0 0 14 14"><path d="M5 2l5 5-5 5" fill="none" stroke="var(--purple)" stroke-width="1.6"/></svg></div>
<div class="abs cat" style="left:150px"><div class="dot" role="img" aria-label="Commercial office interior" style="background:linear-gradient(135deg,#3d3a38,#9b8d7c)"></div>Commercial Office</div>
<div class="abs cat" style="left:311px"><div class="dot" role="img" aria-label="Life sciences workspace" style="background:linear-gradient(135deg,#e8e8ea,#9aa0a8)"></div>Life Sciences</div>
<div class="abs cat" style="left:460px"><div class="dot" role="img" aria-label="Industrial worker on site" style="background:linear-gradient(135deg,#1f2a44,#b8bfca)"></div>Industrial</div>
<div class="abs cat" style="left:609px"><div class="dot" role="img" aria-label="Students in a classroom" style="background:linear-gradient(135deg,#4a3a30,#c4a486)"></div>Education</div>
<div class="abs cat" style="left:758px"><div class="dot" role="img" aria-label="Living room interior" style="background:linear-gradient(135deg,#d6d2cc,#8f8579)"></div>Interiors</div>
<div class="abs cat" style="left:907px"><div class="dot" role="img" aria-label="Healthcare team at work" style="background:linear-gradient(135deg,#f0e8e4,#c48b7d)"></div>Healthcare</div>
<div class="photo reno-photo" role="img" aria-label="Bright renovated hallway with a white staircase and framed walls"></div>
<div class="abs reno-bar"></div>
<div class="btn get-started">Get Started<svg viewBox="0 0 24 10"><path d="M0 5h22M17 1l5 4-5 4" fill="none" stroke="currentColor" stroke-width="1.5"/></svg></div>
<div class="btn learn-more">Learn More<svg viewBox="0 0 24 10"><path d="M0 5h22M17 1l5 4-5 4" fill="none" stroke="currentColor" stroke-width="1.5"/></svg></div>

<!-- architectural -->
<section class="abs arch"></section>
<div class="abs eyebrow" style="left:160px;top:2570px;color:var(--purple-soft)">Home builders based in the Waikato</div>
<h2 class="abs about-h serif" style="left:160px;top:2604px">We are architectural</h2>
<p class="abs about-copy arch-copy" style="left:160px;top:2658px;width:405px">When you build a new home you should expect an excep-tional outcome.<br>Choosing Tarn-Holloway Construction to build your new archi-tectural home, means exceptional workmanship comes as standard and we will work with you to achieve your goals.<br>We simply don't know any other way.<br>All our new homes come with a Homecraft Guild 10 Year Guarantee.</p>
<div class="btn arch-cta">Contact Us<svg viewBox="0 0 24 10"><path d="M0 5h22M17 1l5 4-5 4" fill="none" stroke="currentColor" stroke-width="1.5"/></svg></div>
<div class="photo arch-photo" role="img" aria-label="Modern living room with white leather sofa and black coffee table"></div>

<!-- testimonials -->
<h2 class="abs testi-h serif">CUSTOMER TESTIMONIALS</h2>
<p class="abs testi-sub">Testimonials</p>
<div class="abs arrow-circ" style="left:87px;top:3444px;width:42px;height:42px"><svg viewBox="0 0 14 14"><path d="M9 2L4 7l5 5" fill="none" stroke="var(--purple)" stroke-width="1.6"/></svg></div>
<div class="abs arrow-circ" style="left:1070px;top:3444px;width:42px;height:42px"><svg viewBox="0 0 14 14"><path d="M5 2l5 5-5 5" fill="none" stroke="var(--purple)" stroke-width="1.6"/></svg></div>
<div class="abs testi-card"></div>
<div class="abs quote-mark serif">&ldquo;</div>
<div class="abs stars">
  <svg viewBox="0 0 24 24"><path d="M12 2l3 7 7 .6-5.4 4.7 1.7 7.2L12 17.8 5.7 21.5l1.7-7.2L2 9.6 9 9z" fill="#f2b53a"/></svg>
  <svg viewBox="0 0 24 24"><path d="M12 2l3 7 7 .6-5.4 4.7 1.7 7.2L12 17.8 5.7 21.5l1.7-7.2L2 9.6 9 9z" fill="#f2b53a"/></svg>
  <svg viewBox="0 0 24 24"><path d="M12 2l3 7 7 .6-5.4 4.7 1.7 7.2L12 17.8 5.7 21.5l1.7-7.2L2 9.6 9 9z" fill="#f2b53a"/></svg>
  <svg viewBox="0 0 24 24"><path d="M12 2l3 7 7 .6-5.4 4.7 1.7 7.2L12 17.8 5.7 21.5l1.7-7.2L2 9.6 9 9z" fill="none" stroke="#f2b53a" stroke-width="1.5"/></svg>
  <svg viewBox="0 0 24 24"><path d="M12 2l3 7 7 .6-5.4 4.7 1.7 7.2L12 17.8 5.7 21.5l1.7-7.2L2 9.6 9 9z" fill="none" stroke="#f2b53a" stroke-width="1.5"/></svg>
</div>
<p class="abs testi-copy" style="top:3432px">Lorem ipsum dolor sit amet, consectetur adipiscing elit, sed do eiusmod tempor incididunt ut labore et dolore magna aliqua. Quis ipsum suspendisse ultrices gravi-da. Risus commodo viverra maecenas accumsan lacus vel facilisis.</p>
<p class="abs testi-copy" style="top:3530px">Lorem ipsum dolor sit amet, consectetur adipiscing elit, sed do eiusmod tempor incididunt ut .</p>
<div class="abs avatar" role="img" aria-label="Customer portrait"></div>
<div class="abs who">- MARA ELLISON<small>Ashford, Oregon</small></div>
<div class="photo testi-photo" role="img" aria-label="Grey sofa with patterned cushions and framed artwork"></div>

<!-- footer -->
<footer class="abs footer"></footer>
<div class="abs foot-brand"><i></i>Kestrel Joinery Works</div>
<p class="abs foot-copy">Lorem ipsum dolor sit amet, consectetur adipiscing elit, sed do eiusmod tempor in-cididunt ut labore et dolore magna aliqua. Quis ipsum suspendisse ultrices gravida. Risus commodo viverra maecenas ac-cumsan lacus vel facilisis.</p>
<h3 class="abs foot-h" style="left:558px">Quick Links</h3>
<span class="abs foot-link" style="top:3938px">Home</span>
<span class="abs foot-link" style="top:3976px">About Us</span>
<span class="abs foot-link" style="top:4013px">Renovations</span>
<span class="abs foot-link" style="top:4051px">Contact Us</span>
<h3 class="abs foot-h" style="left:803px">Contact Info</h3>
<div class="abs info" style="top:3936px"><svg viewBox="0 0 24 24"><path d="M12 22s7-7 7-12a7 7 0 0 0-14 0c0 5 7 12 7 12z" fill="none" stroke="#fff" stroke-width="1.6"/><circle cx="12" cy="10" r="2.5" fill="none" stroke="#fff" stroke-width="1.6"/></svg><span>Address1, Address2, Address3, Address4.</span></div>
<div class="abs info" style="top:4017px"><svg viewBox="0 0 24 24"><path d="M5 3h4l2 5-2.5 1.5a11 11 0 0 0 6 6L16 13l5 2v4a2 2 0 0 1-2 2A16 16 0 0 1 3 5a2 2 0 0 1 2-2z" fill="none" stroke="#fff" stroke-width="1.6"/></svg><span>0123456789</span></div>
<div class="abs info" style="top:4066px"><svg viewBox="0 0 24 24"><rect x="3" y="5" width="18" height="14" fill="none" stroke="#fff" stroke-width="1.6"/><path d="M3 6l9 7 9-7" fill="none" stroke="#fff" stroke-width="1.6"/></svg><span>info@kestreljoinery.example</span></div>
<div class="abs foot-line"></div>
<span class="abs legal" style="left:160px">© 2023 - All Rights Reserved By Kestrel Joinery Works Renovations Construction</span>
<span class="abs legal" style="left:842px">PRIVACY TERMS</span>
<span class="abs legal" style="left:963px">|</span>
<span class="abs legal" style="left:986px">TERMS &amp; CONDITIONS</span>

</body>
</html>
```